Kestrel Works Business Cards

This job is for the design of a business card.
I would like to review the design in 2x colour tones to choose from black and white inverted.
EG:
Black with white logo and white with black logo on BACK
White with black text on front and black with white text options
PRINTING DIMENSIONS: 4.5 x 8.5cm
Complete design will need to be provided in ready to print format with bleed lines
Target Market(s)
The audience of my business are people in the trade industry.
It will be also used for general networking with trades people and possible future clients.
I want to be represented as a professional, dynamic, creative and personable operator.
The card should reflect style, taste, experience, professionalism.
Industry/Entity Type
Business
Requirements
Must have
- BACK CONTENT:
- Logo in white and black background and vice versa with WHITE card and black logo review samples.
- FRONT CARD CONTENT:
- Name: Morgan Telvane
- Director
- Phone: 0438 216 947
- Email: morgan@kestrelworks.com.au
- Web: kestrelworks.com.au
- LICENCE #: KT-R 72158
Nice to have
- Possibly a textured background design on rear as a pose to a solid black
- Possibly adding a blue or orange discreet colour tone (possibly for email, phone abbreviated letter or symbols).

```html
<!DOCTYPE html>
<html lang="en">
<head>
<meta charset="utf-8">
<title>Kestrel Works Business Cards</title>
<link rel="stylesheet" href="https://fonts.googleapis.com/css2?family=Open+Sans:wght@400;700&display=swap">
<style>
  :root {
    --ink: #231f20;
    --paper: #ffffff;
    --accent: #f26522;
    --stage: #ffffff;
    --shadow: rgba(0, 0, 0, 0.45);
  }
  html, body {
    margin: 0;
    padding: 0;
    width: 1200px;
    height: 1000px;
    overflow: hidden;
    background: var(--stage);
    font-family: "Open Sans", Arial, sans-serif;
  }
  .sheet { position: relative; width: 1200px; height: 1000px; }

  .card {
    position: absolute;
    width: 518px;
    height: 275px;
    border-radius: 30px;
    overflow: hidden;
    box-shadow: 6px 8px 10px var(--shadow);
  }
  .card--front { left: 55px; }
  .card--back { left: 613px; }
  .row-1 { top: 170px; }
  .row-2 { top: 541px; }

  .card__top, .card__bottom { position: absolute; left: 0; width: 100%; }
  .card__top { top: 0; height: 137px; }
  .card__bottom { top: 137px; bottom: 0; }

  /* Light option: white top, black bottom on front; black top, white bottom on back */
  .theme-light.card--front .card__top { background: var(--paper); color: var(--ink); }
  .theme-light.card--front .card__bottom { background: var(--ink); color: var(--paper); }
  .theme-light.card--back .card__top { background: var(--ink); }
  .theme-light.card--back .card__bottom { background: var(--paper); }

  /* Dark option: colours inverted */
  .theme-dark.card--front .card__top { background: var(--ink); color: var(--paper); }
  .theme-dark.card--front .card__bottom { background: var(--paper); color: var(--ink); }
  .theme-dark.card--back .card__top { background: var(--paper); }
  .theme-dark.card--back .card__bottom { background: var(--ink); }

  .brand-name {
    position: absolute;
    left: 27px;
    top: 52px;
    margin: 0;
    font-size: 37px;
    font-weight: 400;
    letter-spacing: 1px;
    line-height: 1;
    color: inherit;
    text-transform: uppercase;
  }

  .contact-list {
    position: absolute;
    left: 33px;
    top: 13px;
    margin: 0;
    padding: 0;
    list-style: none;
  }
  .contact-list li {
    display: flex;
    align-items: center;
    height: 20px;
    margin-bottom: 6px;
    font-size: 13px;
    line-height: 20px;
    color: inherit;
  }
  .contact-list svg {
    display: block;
    width: 22px;
    height: 20px;
    margin-right: 12px;
    flex: none;
  }

  .skyline {
    position: absolute;
    left: 47px;
    top: 42px;
    width: 426px;
    height: 90px;
  }
  .theme-light .skyline { background: linear-gradient(to bottom, #5a5657 0%, #e6e6e6 60%, #ffffff 100%); }
  .theme-dark .skyline { background: linear-gradient(to bottom, #c9c9c9 0%, #4a4647 60%, #231f20 100%); }

  .licence {
    position: absolute;
    left: 0;
    right: 0;
    top: 10px;
    margin: 0;
    text-align: center;
    font-size: 17px;
    font-weight: 700;
    color: var(--accent);
    letter-spacing: 0.2px;
  }
</style>
</head>
<body>
<main class="sheet">

  <section class="card card--front theme-light row-1" aria-label="Card front, light option">
    <div class="card__top">
      <h1 class="brand-name">Kestrel Works</h1>
    </div>
    <div class="card__bottom">
      <ul class="contact-list">
        <li><svg viewBox="0 0 22 20" aria-hidden="true"><circle cx="11" cy="5.5" r="4" fill="none" stroke="var(--accent)" stroke-width="1.8"/><path d="M2 19 V14 Q2 11 6 11 H16 Q20 11 20 14 V19 Z" fill="none" stroke="var(--accent)" stroke-width="1.8"/><line x1="13" y1="15" x2="17" y2="15" stroke="var(--accent)" stroke-width="1.6"/></svg>Morgan Telvane, Director</li>
        <li><svg viewBox="0 0 22 20" aria-hidden="true"><rect x="1.5" y="3.5" width="19" height="13" fill="none" stroke="var(--accent)" stroke-width="1.8"/><path d="M1.5 3.5 L11 11 L20.5 3.5 M1.5 16.5 L8.5 9 M20.5 16.5 L13.5 9" fill="none" stroke="var(--accent)" stroke-width="1.5"/></svg>morgan@kestrelworks.com.au</li>
        <li><svg viewBox="0 0 22 20" aria-hidden="true"><circle cx="11" cy="10" r="9" fill="none" stroke="var(--accent)" stroke-width="1.8"/><path d="M7.5 5.5 L9.5 5.5 L10 8 L8.8 9 Q10 11.5 12.5 12.6 L13.5 11.4 L16 12 L16 14 Q15.5 15 14 15 Q7 14 6.5 7 Q6.5 5.8 7.5 5.5 Z" fill="var(--accent)"/></svg>0438 216 947</li>
      </ul>
    </div>
  </section>

  <section class="card card--back theme-light row-1" aria-label="Card back, light option">
    <div class="card__top">
      <div class="skyline" role="img" aria-label="City skyline silhouette"></div>
    </div>
    <div class="card__bottom">
      <p class="licence">LICENCE #: KT-R 72158</p>
    </div>
  </section>

  <section class="card card--front theme-dark row-2" aria-label="Card front, dark option">
    <div class="card__top">
      <h2 class="brand-name">Kestrel Works</h2>
    </div>
    <div class="card__bottom">
      <ul class="contact-list">
        <li><svg viewBox="0 0 22 20" aria-hidden="true"><circle cx="11" cy="5.5" r="4" fill="none" stroke="var(--accent)" stroke-width="1.8"/><path d="M2 19 V14 Q2 11 6 11 H16 Q20 11 20 14 V19 Z" fill="none" stroke="var(--accent)" stroke-width="1.8"/><line x1="13" y1="15" x2="17" y2="15" stroke="var(--accent)" stroke-width="1.6"/></svg>Morgan Telvane, Director</li>
        <li><svg viewBox="0 0 22 20" aria-hidden="true"><rect x="1.5" y="3.5" width="19" height="13" fill="none" stroke="var(--accent)" stroke-width="1.8"/><path d="M1.5 3.5 L11 11 L20.5 3.5 M1.5 16.5 L8.5 9 M20.5 16.5 L13.5 9" fill="none" stroke="var(--accent)" stroke-width="1.5"/></svg>morgan@kestrelworks.com.au</li>
        <li><svg viewBox="0 0 22 20" aria-hidden="true"><circle cx="11" cy="10" r="9" fill="none" stroke="var(--accent)" stroke-width="1.8"/><path d="M7.5 5.5 L9.5 5.5 L10 8 L8.8 9 Q10 11.5 12.5 12.6 L13.5 11.4 L16 12 L16 14 Q15.5 15 14 15 Q7 14 6.5 7 Q6.5 5.8 7.5 5.5 Z" fill="var(--accent)"/></svg>0438 216 947</li>
      </ul>
    </div>
  </section>

  <section class="card card--back theme-dark row-2" aria-label="Card back, dark option">
    <div class="card__top">
      <div class="skyline" role="img" aria-label="City skyline silhouette"></div>
    </div>
    <div class="card__bottom">
      <p class="licence">LICENCE #: KT-R 72158</p>
    </div>
  </section>

</main>
</body>
</html>
```